Wine Label: Corvinte

The project is to create 3 wine labels. The brand name is "Corvinte"

What we need is to have 3 versions: red wine, white wine and rose.

The wine is for young and modern people, between 21 and 31 years old, so it need to be casual, modern and fun, but at the same time it needs to keep the Premiums of a good European wine.

It is from Italy.

Target Market(s)

Young adults, between 21 and 31 years old. wine lovers

Requirements
Must have
• - Modern colors (Black, silver, red, etc.)
• - Clean label
• - Clear font
• - Style
• - The brand + the type of wine (red, white or rose)
Nice to have
• - A symbol to represent the brand
Should not have
• - Many elements
• - No clear fonts
• - No funny colors

```html
<!DOCTYPE html>
<html lang="en">
<head>
<meta charset="utf-8">
<title>Corvinte Wine Labels</title>
<link rel="stylesheet" href="https://fonts.googleapis.com/css2?family=Bebas+Neue&family=Pacifico&display=swap">
<style>
  :root {
    --paper: #ffffff;
    --ink-black: #1e1c19;
    --wine-red: #8c1036;
    --rose-pink: #f86fb1;
    --white-gold: #c9923b;
    --type-light: #ffffff;
    --symbol-tone: rgba(255, 255, 255, 0.9);
  }
  * { margin: 0; padding: 0; box-sizing: border-box; }
  html, body {
    width: 853px;
    height: 1200px;
    overflow: hidden;
    background: var(--paper);
  }
  .board {
    position: relative;
    width: 853px;
    height: 1200px;
    background: var(--paper);
  }
  .label {
    position: absolute;
    top: 456px;
    width: 154px;
    height: 650px;
    overflow: hidden;
    color: var(--type-light);
  }
  .label--red-dark { left: 0; background: var(--ink-black); }
  .label--red-wine { left: 218px; background: var(--ink-black); }
  .label--rose { left: 456px; top: 458px; background: var(--rose-pink); }
  .label--white { left: 698px; background: var(--white-gold); }

  .variety-band {
    position: absolute;
    left: 0;
    width: 100%;
    background: var(--wine-red);
  }
  .label--red-dark .variety-band { top: 14px; height: 100px; }
  .label--red-wine .variety-band { top: 0; height: 450px; }

  .variety-script {
    font-family: "Pacifico", cursive;
    font-size: 34px;
    line-height: 1;
    color: var(--type-light);
  }
  .label--red-dark .variety-script,
  .label--red-wine .variety-script {
    position: absolute;
    left: 0;
    width: 100%;
    text-align: center;
  }
  .label--red-dark .variety-script { top: 26px; }
  .label--red-wine .variety-script { top: 36px; }

  .brand-vertical {
    position: absolute;
    font-family: "Bebas Neue", sans-serif;
    font-size: 78px;
    line-height: 1;
    writing-mode: vertical-rl;
    transform: rotate(180deg);
    letter-spacing: 1px;
  }
  .label--red-dark .brand-vertical { left: 46px; top: 176px; }
  .label--red-wine .brand-vertical { left: 46px; top: 176px; }

  .brand-top {
    position: absolute;
    left: 12px;
    top: 48px;
    font-family: "Bebas Neue", sans-serif;
    font-size: 42px;
    line-height: 1;
    letter-spacing: 0.5px;
  }
  .variety-tag {
    position: absolute;
    right: 2px;
    top: 110px;
    font-family: "Pacifico", cursive;
    font-size: 20px;
    line-height: 1;
  }

  .brand-symbol {
    position: absolute;
    left: 32px;
    top: 478px;
    width: 108px;
    height: 152px;
    background: var(--symbol-tone);
    border-radius: 40px 40px 18px 18px;
  }
</style>
</head>
<body>
<main class="board">

  <section class="label label--red-dark">
    <div class="variety-band"><span class="variety-script">red</span></div>
    <h2 class="brand-vertical">Corvinte</h2>
    <div class="brand-symbol" role="img" aria-label="White silhouette of a kneeling figure, the brand symbol"></div>
  </section>

  <section class="label label--red-wine">
    <div class="variety-band">
      <span class="variety-script">red</span>
      <h2 class="brand-vertical">Corvinte</h2>
    </div>
    <div class="brand-symbol" role="img" aria-label="White silhouette of a kneeling figure, the brand symbol"></div>
  </section>

  <section class="label label--rose">
    <h2 class="brand-top">CORVINTE</h2>
    <span class="variety-tag">rose</span>
    <div class="brand-symbol" role="img" aria-label="White silhouette of a kneeling figure, the brand symbol"></div>
  </section>

  <section class="label label--white">
    <h2 class="brand-top">CORVINTE</h2>
    <span class="variety-tag">white</span>
    <div class="brand-symbol" role="img" aria-label="White silhouette of a kneeling figure, the brand symbol"></div>
  </section>

</main>
</body>
</html>
```